National hospice pharmacy network needs a powerpoint design

We need a power point design for a new company that is creating a network of independent pharmacies to provide medication delivery to hospice patients in their area. We will be providing them with logistics to build a delivery system, software to increase efficiency and the marketing to hospice agencies. The pharmacies will benefit with increasing their patient care, increasing their efficiency and increasing their profits.

Pharmacy

```html
<!DOCTYPE html>
<html lang="en">
<head>
<meta charset="utf-8">
<title>NovaDose – Pharmacy Network Slides</title>
<link rel="stylesheet" href="https://fonts.googleapis.com/css2?family=Carlito:wght@400;700&family=Gelasio:ital,wght@0,400;0,600;1,400&display=swap">
<style>
  :root {
    --green: #3db049;
    --blue: #2257a5;
    --backdrop: #707276;
    --white: #ffffff;
    --ink: #1e1e1e;
    --arrow: #000000;
  }
  * { box-sizing: border-box; margin: 0; padding: 0; }
  html, body { width: 847px; height: 1200px; overflow: hidden; }
  body { background: var(--backdrop); position: relative; font-family: "Carlito", "Calibri", sans-serif; }

  .slide {
    position: absolute; left: 88px; width: 676px; height: 507px;
    background: var(--white);
    box-shadow: 8px 8px 6px rgba(0,0,0,0.55);
  }
  .slide--process { top: 69px; }
  .slide--profits { top: 622px; height: 508px; }

  .slide-number {
    position: absolute; left: 34px; top: 0; width: 39px; height: 34px;
    background: var(--green); color: var(--white);
    font-size: 15px; display: flex; align-items: center; justify-content: center;
  }
  .slide-title {
    position: absolute; left: 0; right: 0; top: 52px; text-align: center;
    font-family: "Gelasio", "Cambria", serif; font-style: italic; font-weight: 400;
    font-size: 25px; color: var(--ink);
  }

  /* Process steps */
  .step-box {
    position: absolute; height: 48px; display: flex; align-items: center; justify-content: center;
    text-align: center; color: var(--white); font-size: 14px; line-height: 1.25; padding: 0 6px;
  }
  .step-circle {
    position: absolute; width: 57px; height: 57px; border-radius: 50%;
    color: var(--white); font-size: 19px; display: flex; align-items: center; justify-content: center;
  }
  .is-green { background: var(--green); }
  .is-blue { background: var(--blue); }
  .flow-arrow { position: absolute; }
  .process-note {
    position: absolute; left: 0; right: 0; top: 330px; text-align: center;
    font-family: "Gelasio", "Cambria", serif; font-weight: 600; font-size: 16px; color: var(--ink);
    padding-left: 8px;
  }

  /* Profit cards */
  .benefit-card {
    position: absolute; top: 136px; width: 158px; height: 231px; border-radius: 22px;
    color: var(--white); text-align: center;
  }
  .benefit-circle {
    position: absolute; left: 22px; top: 15px; width: 114px; height: 114px; border-radius: 50%;
    background: var(--white); color: var(--ink); display: flex; align-items: center; justify-content: center;
    font-family: "Gelasio", "Cambria", serif; font-weight: 600; font-size: 16px; line-height: 1.2;
  }
  .benefit-text { position: absolute; left: 8px; right: 8px; top: 138px; font-size: 15px; line-height: 1.35; }

  /* Footer */
  .brand-name {
    position: absolute; left: 20px; bottom: 22px;
    font-family: "Carlito", "Calibri", sans-serif; font-weight: 700; font-size: 30px;
    color: var(--blue); letter-spacing: -0.5px;
  }
  .footer-band { position: absolute; left: 157px; right: 0; bottom: 34px; height: 11px; display: flex; }
  .footer-band span:first-child { width: 254px; background: var(--blue); }
  .footer-band span:last-child { flex: 1; background: var(--green); }
</style>
</head>
<body>

<section class="slide slide--process">
  <div class="slide-number">2</div>
  <h1 class="slide-title">Easy as 1,2,3…..delivered</h1>

  <div class="step-box is-green" style="left:16px; top:231px; width:197px;">Order entered by hospice</div>
  <div class="step-circle is-green" style="left:78px; top:181px;">1</div>

  <div class="step-box is-blue" style="left:236px; top:232px; width:197px;">Prescription sent to prescriber for signature</div>
  <div class="step-circle is-blue" style="left:298px; top:181px;">2</div>

  <div class="step-box is-green" style="left:462px; top:232px; width:197px;">Prescription sent to pharmacy for filling</div>
  <div class="step-circle is-green" style="left:535px; top:181px;">3</div>

  <svg class="flow-arrow" style="left:214px; top:242px;" width="19" height="24" viewBox="0 0 19 24"><path d="M0 6h9V0l10 12-10 12v-6H0z" fill="var(--arrow)"/></svg>
  <svg class="flow-arrow" style="left:437px; top:242px;" width="19" height="24" viewBox="0 0 19 24"><path d="M0 6h9V0l10 12-10 12v-6H0z" fill="var(--arrow)"/></svg>

  <p class="process-note">Pharmacy delivers prescription</p>

  <div class="brand-name">NovaDose</div>
  <div class="footer-band"><span></span><span></span></div>
</section>

<section class="slide slide--profits">
  <div class="slide-number">3</div>
  <h1 class="slide-title">Increased Profits</h1>

  <div class="benefit-card is-green" style="left:62px;">
    <div class="benefit-circle">Script<br>Volume</div>
    <p class="benefit-text">Hospice prescriptions in you area routed to your pharmacy</p>
  </div>
  <div class="benefit-card is-blue" style="left:248px;">
    <div class="benefit-circle">Marketing</div>
    <p class="benefit-text">We contract with hospices on your behalf</p>
  </div>
  <div class="benefit-card is-green" style="left:435px;">
    <div class="benefit-circle">Delivery</div>
    <p class="benefit-text">You are paid $10 per delivery</p>
  </div>

  <svg class="flow-arrow" style="left:219px; top:231px;" width="25" height="32" viewBox="0 0 25 32"><path d="M0 8h12V0l13 16-13 16v-8H0z" fill="var(--arrow)"/></svg>
  <svg class="flow-arrow" style="left:405px; top:231px;" width="25" height="32" viewBox="0 0 25 32"><path d="M0 8h12V0l13 16-13 16v-8H0z" fill="var(--arrow)"/></svg>

  <div class="brand-name">NovaDose</div>
  <div class="footer-band"><span></span><span></span></div>
</section>

</body>
</html>
```